Feminine colorfull packaging for coconut skin care brand

We need a design that can be used on different types of packaging for beauty products likes creams, oils, etc.
The products that we will launch will be made with one key ingredient of coconut oil + other added ingredients depending on the type of product. The entire marketing will therefore be based on COCONUTS, palmtrees, sand, beach, bronzing on the beach, holiday feeling, nature, femininity, etc. = A Lifestyle brand with a tropical vibe.
Packaging can be a pot for creams, flaskes for lotions, smaller bottles for oils, etc. Mostly the standard packaging used for beauty products.
We would like to use the color pink ( this can be bright or pastel or any tone of pink) to address the feminine side of our product and a tone of blue-green ( pastel, bright or any tone of this color) to accentuate the use of coconut.
Third would be the color white (this can be added through an accent somewhere on the packaging or this can be the brand name that is written in white)
Lastely we would like the packaging to be light, fresh and playfull. Please feel free to use different colors or shapes ( we do not yet have a logo. This can then be designed followed on the packaging)
The design will be printed on plastic packaging. We are open to very creative designs. We are looking for packaging that catches the eye by its design and/or colors, that is different than others, that distinguishes the product because of its packaging design.
Target Market(s)
Women between 20 - 35 years
Industry/Entity Type
Beauty
Colors
Designer to choose colors to be used in the design.
Look and feel

```html
<!DOCTYPE html>
<html lang="en">
<head>
<meta charset="utf-8">
<title>Kokolani — Day Facial Oil packaging</title>
<link rel="stylesheet" href="https://fonts.googleapis.com/css2?family=Josefin+Sans:wght@400;600&family=Barlow:wght@400;500&display=swap">
<style>
  :root {
    --backdrop: #d3e2e9;
    --teal-ink: #0d4a55;
    --pink: #e98aa0;
    --pink-soft: #f3adbd;
    --white: #ffffff;
    --paper: #f4f4f4;
    --grey-text: #8a8a8a;
    --dark-text: #2a2a2a;
    --leaf-green: #20b57a;
    --leaf-blue: #1f4fa8;
  }
  * { margin: 0; padding: 0; box-sizing: border-box; }
  html, body { width: 1200px; height: 1056px; overflow: hidden; background: var(--backdrop); }
  .canvas { position: relative; width: 1200px; height: 1056px; font-family: "Barlow", sans-serif; }

  .brand-wordmark {
    position: absolute; left: 736px; top: 96px;
    font-family: "Josefin Sans", sans-serif; font-weight: 600;
    font-size: 40px; letter-spacing: 22px; color: var(--teal-ink);
  }

  .panel { position: absolute; overflow: hidden; }

  /* Lid */
  .panel-top { left: 440px; top: 180px; width: 300px; height: 240px; }
  .panel-top .lid-pattern { position: absolute; inset: 0; background: var(--pink); }
  .panel-top .lid-name {
    position: absolute; left: 0; right: 0; top: 102px; text-align: center;
    font-family: "Josefin Sans", sans-serif; font-weight: 600; font-size: 26px;
    letter-spacing: 12px; padding-left: 12px; color: var(--white);
  }

  /* Back / info side */
  .panel-side { left: 130px; top: 430px; width: 300px; height: 570px; background: var(--paper); }
  .panel-side .palm-leaf {
    position: absolute; left: 20px; top: 140px; width: 240px; height: 360px;
    background: radial-gradient(ellipse at 50% 45%, rgba(190,200,170,0.55), rgba(244,244,244,0) 70%);
  }
  .side-content { position: relative; padding: 44px 30px 0; text-align: center; }
  .side-name {
    font-family: "Josefin Sans", sans-serif; font-weight: 600; font-size: 24px;
    letter-spacing: 11px; padding-left: 11px; color: var(--pink);
  }
  .product-title {
    margin-top: 26px; font-family: "Josefin Sans", sans-serif; font-weight: 600;
    font-size: 15px; letter-spacing: 4px; color: var(--dark-text);
  }
  .product-subtitle {
    margin-top: 4px; font-family: "Josefin Sans", sans-serif; font-size: 10px;
    letter-spacing: 3px; color: var(--dark-text);
  }
  .ingredients { margin-top: 34px; font-size: 11px; line-height: 1.75; color: var(--grey-text); }
  .ingredients .label { letter-spacing: 1px; }
  .social-row { margin-top: 30px; display: flex; justify-content: center; gap: 8px; }
  .social-dot { width: 24px; height: 24px; border-radius: 50%; background: var(--pink); }
  .contact { margin-top: 12px; font-size: 10px; line-height: 1.5; color: var(--dark-text); font-weight: 500; }
  .contact .handle { letter-spacing: 2px; }
  .cert-row { margin-top: 12px; display: flex; justify-content: center; gap: 12px; }
  .cert-badge { width: 22px; height: 18px; background: var(--dark-text); border-radius: 3px; }

  /* Front */
  .panel-front { left: 440px; top: 430px; width: 300px; height: 570px; background: var(--paper); }
  .panel-front svg { display: block; }
  .front-text { font-family: "Josefin Sans", sans-serif; }

  /* End of second box */
  .panel-end { left: 760px; top: 430px; width: 300px; height: 570px; background: var(--pink); }
  .panel-end .end-pattern { position: absolute; inset: 0; background: var(--pink); }
  .panel-end .end-name {
    position: absolute; left: 150px; top: 285px; transform: translate(-50%, -50%) rotate(90deg);
    white-space: nowrap; font-family: "Josefin Sans", sans-serif; font-weight: 600;
    font-size: 30px; letter-spacing: 14px; color: var(--white);
  }
</style>
</head>
<body>
<main class="canvas">
  <div class="brand-wordmark">KOKOLANI</div>

  <section class="panel panel-top">
    <div class="lid-pattern" role="img" aria-label="Tone-on-tone pink damask pattern"></div>
    <div class="lid-name">KOKOLANI</div>
  </section>

  <section class="panel panel-side">
    <div class="palm-leaf" role="img" aria-label="Faded palm frond photograph"></div>
    <div class="side-content">
      <div class="side-name">KOKOLANI</div>
      <div class="product-title">DAY FACIAL OIL</div>
      <div class="product-subtitle">HUILE DE JOUR POUR<br>LE VISAGE</div>
      <div class="ingredients">
        <span class="label">INGRÉDIENTS:</span><br>
        Perilla Ocymoides<br>(Perilla) Seed Oil*,<br>Camellia Oleifera<br>(Camellia) Seed Oil*,<br>
        Rosa Canina (Rosehip)<br>Fruit Oil*, Borago<br>Officinalis (Borage)<br>Seed Oil*, Simmondsia<br>Chinensis (Jojoba)
      </div>
      <div class="social-row"><span class="social-dot"></span><span class="social-dot"></span></div>
      <div class="contact"><span class="handle">@SoleMarina</span><br>solemarinaorganics.com</div>
      <div class="cert-row"><span class="cert-badge"></span><span class="cert-badge"></span></div>
    </div>
  </section>

  <section class="panel panel-front">
    <svg width="300" height="570" viewBox="0 0 300 570">
      <defs>
        <linearGradient id="leafBand" x1="0" y1="1" x2="1" y2="0">
          <stop offset="0" stop-color="#1f4fa8"/>
          <stop offset="0.55" stop-color="#1f9c9a"/>
          <stop offset="1" stop-color="#20b57a"/>
        </linearGradient>
        <linearGradient id="pinkFade" x1="0" y1="0" x2="0" y2="1">
          <stop offset="0" stop-color="#f3adbd" stop-opacity="0"/>
          <stop offset="1" stop-color="#f3adbd" stop-opacity="0.7"/>
        </linearGradient>
        <radialGradient id="coconut" cx="0.5" cy="0.5" r="0.5">
          <stop offset="0" stop-color="#f5f0e6"/>
          <stop offset="0.5" stop-color="#b07a4a"/>
          <stop offset="1" stop-color="#7a4b2a"/>
        </radialGradient>
      </defs>
      <rect class="pink-block" x="100" y="0" width="200" height="250" fill="#f3adbd"/>
      <text class="front-text" x="204" y="132" text-anchor="middle" fill="#fff" font-size="18" font-weight="600" letter-spacing="7">KOKOLANI</text>
      <polygon points="0,470 300,250 300,360 0,570" fill="url(#leafBand)" role="img" aria-label="Tropical palm leaf photograph in green and blue"/>
      <g transform="rotate(-36 150 410)">
        <text class="front-text" x="150" y="398" text-anchor="middle" fill="#fff" font-size="17" font-weight="600" letter-spacing="4">DAY FACIAL OIL</text>
        <text class="front-text" x="150" y="414" text-anchor="middle" fill="#fff" font-size="10" letter-spacing="3">HUILE DE JOUR POUR</text>
        <text class="front-text" x="150" y="427" text-anchor="middle" fill="#fff" font-size="10" letter-spacing="3">LE VISAGE</text>
      </g>
      <ellipse cx="120" cy="490" rx="55" ry="34" fill="url(#coconut)" role="img" aria-label="Split coconut with splashing coconut milk"/>
      <rect x="0" y="500" width="300" height="70" fill="url(#pinkFade)" role="img" aria-label="Pink halftone dot fade"/>
      <g transform="rotate(-20 215 530)">
        <rect x="153" y="515" width="124" height="30" fill="#fff" opacity="0.85"/>
        <text class="front-text" x="215" y="527" text-anchor="middle" fill="#0d4a55" font-size="8.5" letter-spacing="2">NORMAL SKIN</text>
        <text class="front-text" x="215" y="539" text-anchor="middle" fill="#0d4a55" font-size="8.5" letter-spacing="2">PEAUX NORMALES</text>
      </g>
    </svg>
  </section>

  <section class="panel panel-end">
    <div class="end-pattern" role="img" aria-label="Tone-on-tone pink damask pattern"></div>
    <div class="end-name">KOKOLANI</div>
  </section>
</main>
</body>
</html>
```